Tovesca Website

I need a website for a startup company that provides GIS (Geographic Information Services) staffing and products for local cities. Current website is www.tovescagroup.com

```html
<!DOCTYPE html>
<html lang="en">
<head>
<meta charset="utf-8">
<title>Tovesca Group</title>
<link href="https://fonts.googleapis.com/css2?family=Roboto:wght@400;500;700&family=Rubik:wght@500;700;800&display=swap" rel="stylesheet">
<style>
:root{
  --orange:#ff4a12;
  --orange-deep:#e63d0b;
  --brown:#3b2510;
  --ink:#111111;
  --muted:#6b6b6b;
  --white:#ffffff;
  --soft:#fde9e1;
}
*{margin:0;padding:0;box-sizing:border-box}
html,body{width:1200px;height:3431px;overflow:hidden}
body{position:relative;background:var(--white);font-family:'Roboto',sans-serif;color:var(--ink)}
.abs{position:absolute}
/* header */
.top-line{left:0;top:0;width:1200px;height:4px;background:var(--orange)}
.brand{left:109px;top:28px;font-family:'Rubik',sans-serif;font-weight:700;font-size:31px;color:var(--brown);letter-spacing:.3px}
.nav a{position:absolute;top:38px;font-size:14.5px;font-weight:500;color:#222;text-decoration:none}
.nav a.active{color:var(--orange)}
.contact-btn{left:950px;top:25px;width:138px;height:42px;border-radius:21px;background:var(--brown);color:var(--white);font-size:14.5px;font-weight:500;display:flex;align-items:center;justify-content:center;gap:10px}
/* hero */
.hero-svg{left:0;top:96px}
.hero-kicker{left:0;width:1200px;top:228px;text-align:center;color:var(--white);font-size:23px;font-weight:500}
.hero-title{left:0;width:1200px;top:264px;text-align:center;color:var(--white);font-family:'Rubik',sans-serif;font-weight:800;font-size:47px;letter-spacing:.5px}
.hero-text{left:240px;width:720px;top:328px;text-align:center;color:var(--white);font-size:17.5px;line-height:30px}
.btn{display:flex;align-items:center;justify-content:center;border-radius:22px;font-size:15px;font-weight:500}
.btn-orange{background:var(--orange);color:var(--white)}
.btn-white{background:var(--white);color:var(--orange)}
/* about */
.about-photo{left:111px;top:714px;width:418px;height:418px;border-radius:50%;background:linear-gradient(160deg,#3f6fb8 0%,#6f9ccf 45%,#7f8a5a 70%,#8a7560 100%)}
.about-map{left:355px;top:930px;width:254px;height:254px;border-radius:50%;border:8px solid var(--white);background:radial-gradient(circle at 40% 40%,#2e4a8e,#14204d 75%);box-shadow:0 6px 18px rgba(0,0,0,.18)}
.h2{font-family:'Roboto',sans-serif;font-weight:700;font-size:36px;color:var(--ink);letter-spacing:.3px}
.about-title{left:678px;top:752px}
.about-text{left:678px;top:808px;width:440px;font-size:15.5px;line-height:31px;color:var(--muted)}
.about-lead{left:678px;top:1008px;width:440px;font-size:16px;line-height:29px;color:var(--ink)}
/* services */
.services-title{left:0;width:1200px;top:1258px;text-align:center}
.services-sub{left:0;width:1200px;top:1318px;text-align:center;font-size:20px;color:#555}
.card-photo{width:465px;height:372px;border-radius:22px}
.card-box{width:403px;height:175px;background:var(--white);border-radius:22px;box-shadow:0 18px 40px rgba(0,0,0,.10)}
.card-icon{position:absolute;left:31px;top:41px;width:66px;height:66px;border-radius:50%;background:var(--soft);display:flex;align-items:center;justify-content:center}
.card-title{position:absolute;left:116px;top:36px;font-size:16.5px;font-weight:700;color:var(--ink)}
.card-text{position:absolute;left:116px;top:66px;width:270px;font-size:13.5px;line-height:25px;color:var(--muted)}
/* why */
.why-svg{left:0;top:2430px}
.why-title{left:109px;top:2672px;color:var(--white);font-family:'Rubik',sans-serif;font-weight:700;font-size:36px}
.why-text{left:109px;top:2732px;width:440px;font-size:15.5px;line-height:31px;color:var(--white)}
.why-list{left:134px;top:2838px;list-style:none;color:var(--white);font-size:15.5px}
.why-list li{display:flex;align-items:center;gap:13px;height:31px}
.why-visual{left:606px;top:2567px;width:474px;height:474px;border-radius:50%;background:radial-gradient(circle at 50% 55%,#1e3a5a 0%,#1d1d1f 45%,#1b1b1b 100%)}
/* footer */
.footer-brand{left:0;width:1200px;top:3236px;text-align:center;font-family:'Rubik',sans-serif;font-weight:700;font-size:42px;color:var(--brown)}
.footer-nav a{position:absolute;top:3307px;font-size:14.5px;font-weight:700;color:#222;text-decoration:none}
.footer-nav span{position:absolute;top:3307px;font-size:14px;font-weight:700;color:#222}
.social{top:3350px;width:34px;height:34px;border-radius:50%;background:var(--orange)}
.copyright{left:0;width:1200px;top:3403px;text-align:center;font-size:13px;color:#555}
</style>
</head>
<body>

<header>
  <div class="abs top-line"></div>
  <div class="abs brand">TOVESCA GROUP</div>
  <nav class="nav">
    <a class="active" style="left:457px" href="#">Home</a>
    <a style="left:547px" href="#">About Us</a>
    <a style="left:662px" href="#">Our Services</a>
    <a style="left:800px" href="#">Why Choose Us</a>
  </nav>
  <div class="abs contact-btn">
    <svg width="13" height="13" viewBox="0 0 14 14"><circle cx="7" cy="4" r="3.2" fill="#fff"/><path d="M1 14c0-4 2.7-6 6-6s6 2 6 6z" fill="#fff"/></svg>
    Contact Us
  </div>
</header>

<section class="hero">
  <svg class="abs hero-svg" width="1200" height="560" viewBox="0 0 1200 560">
    <defs>
      <linearGradient id="skyline" x1="0" y1="0" x2="0" y2="1">
        <stop offset="0" stop-color="#5a79a8"/>
        <stop offset=".45" stop-color="#3c4f78"/>
        <stop offset=".75" stop-color="#6a4a66"/>
        <stop offset="1" stop-color="#2c3252"/>
      </linearGradient>
    </defs>
    <path role="img" aria-label="Night city skyline with a tall tower and a domed stadium by the water" d="M0 0H1200V377Q600 603 0 377Z" fill="url(#skyline)"/>
    <path d="M40 398Q600 680 1160 388Q600 600 40 398Z" fill="var(--orange)"/>
  </svg>
  <div class="abs hero-kicker">TOVESCA GROUP</div>
  <h1 class="abs hero-title">WE MAKE GIS WORK FOR YOU</h1>
  <p class="abs hero-text">We are an innovative team of geospatial experts with 25 years of experience in the field of GIS. We specialize in providing results-driven GIS solutions.</p>
  <div class="abs btn btn-orange" style="left:534px;top:413px;width:131px;height:40px">Get Started</div>
</section>

<section class="about">
  <div class="abs about-photo" role="img" aria-label="Surveyor in a safety vest using a GNSS pole on a coastal hillside"></div>
  <div class="abs about-map" role="img" aria-label="Dark blue digital map with location pins"></div>
  <h2 class="abs h2 about-title">ABOUT US</h2>
  <p class="abs about-text">Sed ut perspiciatis unde omnis iste natus error sit voluptatem accusantium doloremque laudantium, totam rem aperiam, eaque ipsa quae ab illo inventore veritatis et quasi architecto beatae vitae dicta sunt explicabo. Nemo enim ipsam voluptatem quia voluptas sit aspernatur aut odit aut fugit, sed quia consequuntur magni</p>
  <p class="abs about-lead">We specialize in providing results-driven GIS solutions for local government and the private sector.</p>
  <div class="abs btn btn-orange" style="left:678px;top:1087px;width:130px;height:42px">Read More</div>
</section>

<section class="services">
  <h2 class="abs h2 services-title">SERVICES WE PROVIDE</h2>
  <p class="abs services-sub">Ut enim ad minima veniam, quis nostrum exercitationem ullam corporis suscipit laboriosam.</p>

  <div class="abs card-photo" style="left:105px;top:1384px;background:linear-gradient(150deg,#6b5a4c,#c9bdaf 55%,#3a3634)" role="img" aria-label="Team reviewing plans and a tablet around a desk"></div>
  <div class="abs card-photo" style="left:630px;top:1384px;background:linear-gradient(160deg,#2d6fb6,#5ba3dc 50%,#3f86c9)" role="img" aria-label="Finger tracing a route on a blue road map"></div>
  <div class="abs card-photo" style="left:105px;top:1891px;background:linear-gradient(150deg,#4a4440,#c8c0b6 50%,#d2693a 80%,#6b5d52)" role="img" aria-label="Hand sketching on drawings beside an orange hard hat"></div>
  <div class="abs card-photo" style="left:630px;top:1891px;background:linear-gradient(150deg,#e4e1dc,#9ea3a8 50%,#2a2b2f)" role="img" aria-label="Engineer working on 3D models at a computer screen"></div>

  <div class="abs card-box" style="left:136px;top:1658px">
    <div class="card-icon"><svg width="30" height="30" viewBox="0 0 30 30" fill="var(--orange)"><ellipse cx="13" cy="6" rx="10" ry="4"/><path d="M3 9c0 2.2 4.5 4 10 4s10-1.8 10-4v4c0 2.2-4.5 4-10 4S3 15.2 3 13z"/><path d="M3 16c0 2.2 4.5 4 10 4v4C7.5 24 3 22.2 3 20z"/><circle cx="22" cy="22" r="5" fill="none" stroke="var(--orange)" stroke-width="2.4"/></svg></div>
    <div class="card-title">GIS CONSULTING</div>
    <p class="card-text">Sed ut perspiciatis unde omnis iste natus error sit voluptatem accusantium dolor emque laudantium, totam rem</p>
  </div>
  <div class="abs card-box" style="left:661px;top:1658px">
    <div class="card-icon"><svg width="24" height="28" viewBox="0 0 24 28"><path d="M2 0h14l6 6v22H2z" fill="var(--orange)"/><g stroke="#fff" stroke-width="2"><path d="M7 11h10M7 15h10M7 19h10M7 23h6"/></g></svg></div>
    <div class="card-title">GIS APPLICATIONS</div>
    <p class="card-text">Sed ut perspiciatis unde omnis iste natus error sit voluptatem accusantium dolor emque laudantium, totam rem</p>
  </div>
  <div class="abs card-box" style="left:136px;top:2166px">
    <div class="card-icon"><svg width="32" height="28" viewBox="0 0 32 28" fill="var(--orange)"><path d="M10 6h20v14H10z"/><path d="M4 12h6v8H2v-4z"/><circle cx="9" cy="23" r="4"/><circle cx="25" cy="23" r="4"/></svg></div>
    <div class="card-title">SPATIAL DATA SOLUTIONS</div>
    <p class="card-text">Sed ut perspiciatis unde omnis iste natus error sit voluptatem accusantium dolor emque laudantium, totam rem</p>
  </div>
  <div class="abs card-box" style="left:661px;top:2166px">
    <div class="card-icon"><svg width="30" height="28" viewBox="0 0 30 28" fill="var(--orange)"><path d="M2 6h9l3 3h14v17H2z"/><path d="M8 2h12l4 4v3H8z" opacity=".7"/></svg></div>
    <div class="card-title">SYSTEM ARCHITECTURE DESIGN</div>
    <p class="card-text">Sed ut perspiciatis unde omnis iste natus error sit voluptatem accusantium dolor emque laudantium, totam rem</p>
  </div>
</section>

<section class="why">
  <svg class="abs why-svg" width="1200" height="790" viewBox="0 0 1200 790">
    <path d="M100 128Q620 -40 1170 126" fill="none" stroke="var(--brown)" stroke-width="14"/>
    <path d="M0 170Q520 40 1200 150V614Q600 840 0 614Z" fill="var(--orange)"/>
    <path d="M30 628Q560 880 1100 636" fill="none" stroke="var(--brown)" stroke-width="12"/>
  </svg>
  <div class="abs why-visual" role="img" aria-label="Hand holding a glowing globe pin above a digital grid"></div>
  <h2 class="abs why-title">WHY CHOOSE US</h2>
  <p class="abs why-text">Sed ut perspiciatis unde omnis iste natus error sit voluptatem accusantium doloremque laudantium, totam rem aperiam, eaque ipsa quae ab illo inventore</p>
  <ul class="abs why-list">
    <li><svg width="14" height="14" viewBox="0 0 14 14"><circle cx="7" cy="7" r="7" fill="#fff"/><path d="M4 7h5M7 4.5 9.5 7 7 9.5" stroke="var(--orange)" stroke-width="1.8" fill="none"/></svg>Quis autem vel eum iure reprehenderit qui in ea</li>
    <li><svg width="14" height="14" viewBox="0 0 14 14"><circle cx="7" cy="7" r="7" fill="#fff"/><path d="M4 7h5M7 4.5 9.5 7 7 9.5" stroke="var(--orange)" stroke-width="1.8" fill="none"/></svg>Voluptate velit esse quam nihil</li>
    <li><svg width="14" height="14" viewBox="0 0 14 14"><circle cx="7" cy="7" r="7" fill="#fff"/><path d="M4 7h5M7 4.5 9.5 7 7 9.5" stroke="var(--orange)" stroke-width="1.8" fill="none"/></svg>Dolorem eum fugiat quo voluptas nulla pariatur</li>
  </ul>
  <div class="abs btn btn-white" style="left:109px;top:2953px;width:131px;height:43px">Read More</div>
</section>

<footer>
  <div class="abs footer-brand">TOVESCA GROUP</div>
  <nav class="footer-nav">
    <a style="left:284px" href="#">HOME</a><span style="left:378px">|</span>
    <a style="left:434px" href="#">ABOUT US</a><span style="left:558px">|</span>
    <a style="left:615px" href="#">OUR SERVICES</a><span style="left:771px">|</span>
    <a style="left:827px" href="#">CONTACT US</a>
  </nav>
  <div class="abs social" style="left:541px" aria-label="Social link"></div>
  <div class="abs social" style="left:584px" aria-label="Social link"></div>
  <div class="abs social" style="left:626px" aria-label="Social link"></div>
  <div class="abs copyright">(C) Copyright 2024 | All Rights Reserved</div>
</footer>

</body>
</html>
```